依頼詳細
TOPページのイメージは変更せずに、最近導入したVRでの物件紹介や販売物件のページを増やしたい。VRのコンテンツについては、URLを組み込めるので、自社でカスタマイズできるようにしてほしい。
また、現在のTOPページを超える斬新なデザインを提案していただければ採用も検討します。
サイトURL
http://k-r-t.example.jp
ページ数
2ページ
希望イメージ
シンプル 複雑
単色 カラフル
暗い 明るい
日常 高級
遊び心 厳粛
未来的 伝統的
女性的 男性的
希望する色
納品ファイル
補足説明
以前に別法人のロゴをコンペ形式で募集した内容です。
参考までに↓
https://www.sakuhinba.example.jp/work/detail/503927
依頼金額を99320円に変更して、延長しました。
提案者が少なすぎて残念に思っております。
漠然とし過ぎた依頼なのかもしれませんが、デザイン性だけでも比較してみたいのが理由です。
期限時間ギリギリで1件の応募で、キャンセルするにしても全額お一人だけに配分することが納得いきませんので、何人かに配分出来ればと思い延長させて頂きました。
同じ方からの度重なる提案は受け入れ難く思っております。
これぞという提案でご参加いただきますようご配慮くださいませ。
仙台の街並み等の風景は個人的に好きではありません。
仙台が本社ではありますが、商圏は全国ですのであまり仙台を意識しないデザインでお願いします。

細かい部分はさておき、私の好みをなんとなく汲み取って頂いたようなので選ばせていただきました。

ご提案頂いた皆様ありがとうございました。

```html
<!DOCTYPE html>
<html lang="ja">
<head>
<meta charset="utf-8">
<title>SELECTA 不動産</title>
<link href="https://fonts.googleapis.com/css2?family=Montserrat:wght@500;700;800;900&family=Noto+Sans+JP:wght@400;500;700&display=swap" rel="stylesheet">
<style>
:root{
  --orange:#ff8a2b;
  --orange-deep:#ff7a35;
  --coral:#ff6b62;
  --navy:#1c1f37;
  --navy-soft:#2a2e4c;
  --ink:#2b2b33;
  --muted:#8a8a92;
  --line:#e4e4e8;
  --gray-bg:#efeff1;
  --white:#ffffff;
}
*{margin:0;padding:0;box-sizing:border-box}
html,body{width:1200px;height:3596px;overflow:hidden}
body{position:relative;background:var(--white);font-family:"Noto Sans JP",sans-serif;color:var(--ink)}
.en{font-family:"Montserrat",sans-serif}

/* hero + header */
.hero{position:absolute;left:0;top:0;width:1200px;height:680px;background:linear-gradient(180deg,var(--orange) 0%,var(--orange-deep) 60%,#ff8a55 100%)}
.hero::after{content:"";position:absolute;left:0;bottom:0;width:100%;height:200px;background:linear-gradient(180deg,rgba(255,255,255,0),rgba(255,255,255,.9))}
.site-header{position:absolute;left:0;top:0;width:1200px;height:100px}
.brand{position:absolute;left:108px;top:34px;font-family:"Montserrat",sans-serif;font-weight:900;font-size:28px;color:var(--white);letter-spacing:1px}
.global-nav{position:absolute;left:380px;top:44px;display:flex;gap:26px}
.global-nav a{color:var(--white);font-size:12px;text-decoration:none;font-weight:500}
.header-btn{position:absolute;top:36px;height:32px;border-radius:16px;font-size:11.5px;display:flex;align-items:center;justify-content:center;font-weight:700}
.btn-request{left:780px;width:190px;background:rgba(255,255,255,.22);color:var(--white)}
.btn-login{left:980px;width:110px;background:var(--white);color:var(--orange-deep)}
.hero-title{position:absolute;left:160px;top:292px;font-family:"Montserrat",sans-serif;font-weight:900;font-size:84px;color:var(--white);line-height:1;letter-spacing:2px;z-index:2}
.hero-sub{position:absolute;left:162px;top:392px;font-size:15px;color:var(--white);font-weight:700;z-index:2}
.hero-by{position:absolute;left:400px;top:380px;font-family:"Montserrat",sans-serif;font-weight:700;font-size:40px;color:var(--white);z-index:2}
.skyline{position:absolute;left:560px;top:110px;width:500px;height:470px;background:linear-gradient(180deg,rgba(255,255,255,.05),rgba(255,255,255,.3));border-radius:4px;z-index:1}

/* search */
.search-bar{position:absolute;left:150px;top:690px;width:900px;height:70px;background:var(--navy);border-radius:4px;display:flex;align-items:center;padding:0 16px;gap:12px;z-index:3}
.search-label{color:var(--white);font-size:13px;font-weight:700;width:90px;display:flex;align-items:center;gap:8px}
.search-select{height:38px;background:var(--white);border-radius:3px;width:190px;font-size:12px;display:flex;align-items:center;justify-content:space-between;padding:0 12px;color:var(--ink)}
.search-btn{height:38px;width:170px;background:var(--navy-soft);border:1px solid #4a4f72;border-radius:3px;color:var(--white);font-size:12px;display:flex;align-items:center;justify-content:center;gap:8px}

/* headings */
.section-title{position:absolute;left:0;width:1200px;text-align:center;font-family:"Montserrat",sans-serif;font-weight:800;font-size:28px;color:var(--navy);letter-spacing:1px}
.section-kana{position:absolute;left:0;width:1200px;text-align:center;font-size:11px;color:var(--white)}
.on-dark{color:var(--white)}

/* information */
.info-label{position:absolute;left:150px;top:868px;font-size:12px;font-weight:700;color:var(--ink)}
.info-list{position:absolute;left:150px;top:900px;width:900px;list-style:none}
.info-item{display:flex;gap:26px;padding:14px 0;border-bottom:1px solid var(--line);height:80px}
.info-date{width:90px;font-size:10px;color:var(--muted);font-family:"Montserrat",sans-serif}
.info-body h3{font-size:12px;font-weight:700;margin-bottom:6px}
.info-body h3 .new{display:inline-block;background:var(--coral);color:var(--white);font-size:9px;padding:1px 6px;border-radius:2px;margin-left:8px;vertical-align:middle}
.info-body p{font-size:10.5px;color:#66666e;line-height:1.6}
.pill-btn{position:absolute;width:170px;height:38px;border-radius:19px;background:var(--navy);color:var(--white);font-family:"Montserrat",sans-serif;font-weight:700;font-size:11px;display:flex;align-items:center;justify-content:center;letter-spacing:1px}

/* property grids */
.rent{position:absolute;left:0;top:1260px;width:1200px;height:760px;background:linear-gradient(90deg,var(--orange) 0%,var(--coral) 100%)}
.sale{position:absolute;left:0;top:2020px;width:1200px;height:700px;background:var(--gray-bg)}
.grid{position:absolute;left:150px;width:900px;display:grid;grid-template-columns:repeat(3,1fr);gap:4px}
.card{background:var(--white)}
.photo{height:215px}
.caption{height:56px;padding:12px 14px}
.caption strong{display:block;font-size:12px;font-weight:700}
.caption span{display:block;font-family:"Montserrat",sans-serif;font-size:8.5px;color:var(--muted);margin-top:3px;letter-spacing:.5px}

/* office */
.office-photo{position:absolute;border-radius:2px}
.office-info{position:absolute;width:300px}
.office-info h3{font-size:20px;font-weight:700;margin-bottom:14px}
.office-info p{font-size:12px;line-height:1.8;color:#44444c}
.map-btn{width:110px;height:30px;font-size:10px;position:static;margin-top:18px}

/* footer */
.site-footer{position:absolute;left:0;top:3460px;width:1200px;height:136px;background:var(--navy)}
.footer-brand{position:absolute;left:108px;top:38px;font-family:"Montserrat",sans-serif;font-weight:900;font-size:26px;color:var(--white)}
.footer-nav{position:absolute;left:340px;top:48px;display:flex;gap:24px}
.footer-nav a{color:var(--white);font-size:11px;text-decoration:none}
.copyright{position:absolute;left:0;top:104px;width:1200px;text-align:center;font-family:"Montserrat",sans-serif;font-size:9px;color:#8a8ca6}
.to-top{position:absolute;left:1128px;top:3404px;width:40px;height:40px;border:1px solid var(--orange);background:var(--white);display:flex;align-items:center;justify-content:center}
</style>
</head>
<body>

<section class="hero">
  <header class="site-header">
    <div class="brand">SELECTA</div>
    <nav class="global-nav">
      <a href="#">物件検索</a><a href="#">不動産売却・買取</a><a href="#">オーナー様へ</a><a href="#">会社概要</a>
    </nav>
    <div class="header-btn btn-request">物件リクエスト・お問合せ</div>
    <div class="header-btn btn-login">会員ログイン</div>
  </header>
  <div class="skyline" role="img" aria-label="線画で描かれた高層ビルの街並みのイラスト"></div>
  <h1 class="hero-title">SELECTA</h1>
  <p class="hero-sub">デジタル時代の不動産を見つける</p>
  <p class="hero-by">by Morimoto</p>
</section>

<form class="search-bar">
  <div class="search-label">
    <svg width="16" height="16" viewBox="0 0 16 16"><circle cx="7" cy="7" r="5" fill="none" stroke="#fff" stroke-width="2"/><line x1="11" y1="11" x2="15" y2="15" stroke="#fff" stroke-width="2"/></svg>物件検索
  </div>
  <div class="search-select">賃貸物件<svg width="8" height="6"><path d="M0 0 L8 0 L4 6z" fill="#888"/></svg></div>
  <div class="search-select">マンション・アパート<svg width="8" height="6"><path d="M0 0 L8 0 L4 6z" fill="#888"/></svg></div>
  <div class="search-btn"><svg width="12" height="14" viewBox="0 0 12 14"><path d="M6 0a5 5 0 0 1 5 5c0 4-5 9-5 9S1 9 1 5a5 5 0 0 1 5-5z" fill="#fff"/></svg>エリアから探す</div>
  <div class="search-btn"><svg width="12" height="14" viewBox="0 0 12 14"><rect x="1" y="0" width="10" height="11" rx="2" fill="#fff"/><line x1="2" y1="14" x2="4" y2="11" stroke="#fff"/><line x1="10" y1="14" x2="8" y2="11" stroke="#fff"/></svg>路線から探す</div>
</form>

<section class="information">
  <h2 class="section-title" style="top:810px">INFOMATION</h2>
  <p class="info-label">お知らせ情報</p>
  <ul class="info-list">
    <li class="info-item"><span class="info-date">2024.03.15</span><div class="info-body"><h3>VR内覧サービスのご案内<span class="new">NEW</span></h3><p>一部の物件でVRによる内覧が可能になりました。ご来店前にお部屋の様子をご確認いただけます。</p></div></li>
    <li class="info-item"><span class="info-date">2024.02.28</span><div class="info-body"><h3>年末年始休業のお知らせ</h3><p>誠に勝手ながら下記の期間を休業とさせていただきます。期間中のお問い合わせは休業明けに順次ご対応いたします。</p></div></li>
    <li class="info-item"><span class="info-date">2024.01.10</span><div class="info-body"><h3>新規物件掲載のお知らせ</h3><p>賃貸・売買ともに新しい物件を多数掲載いたしました。詳しくは物件検索ページよりご覧ください。</p></div></li>
  </ul>
  <div class="pill-btn" style="left:515px;top:1170px">VIEW MORE</div>
</section>

<section class="rent">
  <h2 class="section-title on-dark" style="top:62px">FOR RENT</h2>
  <p class="section-kana" style="top:98px">賃貸物件</p>
  <div class="grid" style="top:130px">
    <div class="card"><div class="photo" role="img" aria-label="マンションの外観写真" style="background:linear-gradient(160deg,#b9c3cc,#6d7884)"></div><div class="caption"><strong>マンション・アパート</strong><span>MANSION APARTMENT</span></div></div>
    <div class="card"><div class="photo" role="img" aria-label="一戸建て住宅と青空の写真" style="background:linear-gradient(180deg,#7fa9d6,#c9c6bd 70%,#8b9a6d)"></div><div class="caption"><strong>一戸建て</strong><span>DETACHED HOUSE</span></div></div>
    <div class="card"><div class="photo" role="img" aria-label="空き地の写真" style="background:linear-gradient(180deg,#a9c4df,#b6a57d 55%,#9a8a60)"></div><div class="caption"><strong>土地</strong><span>LAND</span></div></div>
    <div class="card"><div class="photo" role="img" aria-label="シャッターの並ぶ店舗の写真" style="background:linear-gradient(180deg,#d9dadc,#9b9da2)"></div><div class="caption"><strong>店舗・事務所</strong><span>SHOP OFFICE</span></div></div>
    <div class="card"><div class="photo" role="img" aria-label="高層オフィスビルの写真" style="background:linear-gradient(180deg,#9fc0e0,#4d6f93)"></div><div class="caption"><strong>ビル</strong><span>BUILDING</span></div></div>
    <div class="card"><div class="photo" role="img" aria-label="車が並ぶ駐車場の写真" style="background:linear-gradient(180deg,#c7ccd3,#5f6670)"></div><div class="caption"><strong>駐車場</strong><span>PARKING</span></div></div>
  </div>
</section>

<section class="sale">
  <h2 class="section-title" style="top:62px">FOR SALE</h2>
  <p class="section-kana" style="top:98px;color:var(--muted)">売買物件</p>
  <div class="grid" style="top:130px">
    <div class="card"><div class="photo" role="img" aria-label="分譲マンションの外観写真" style="background:linear-gradient(180deg,#9cc0e2,#b8a48c)"></div><div class="caption"><strong>マンション・アパート</strong><span>MANSION APARTMENT</span></div></div>
    <div class="card"><div class="photo" role="img" aria-label="新築一戸建ての写真" style="background:linear-gradient(180deg,#c4d6e6,#d8d2c4 60%,#7f9a62)"></div><div class="caption"><strong>一戸建て</strong><span>DETACHED HOUSE</span></div></div>
    <div class="card"><div class="photo" role="img" aria-label="住宅地の空き地の写真" style="background:linear-gradient(180deg,#8fb3d8,#a38d66 60%,#7d6c4c)"></div><div class="caption"><strong>土地</strong><span>LAND</span></div></div>
    <div class="card"><div class="photo" role="img" aria-label="白い内装の空き店舗の写真" style="background:linear-gradient(180deg,#f2f2f0,#c9c9c6)"></div><div class="caption"><strong>店舗・事務所</strong><span>SHOP OFFICE</span></div></div>
    <div class="card"><div class="photo" role="img" aria-label="ガラス張りの高層ビルの写真" style="background:linear-gradient(180deg,#a6c6e6,#5a7c9f)"></div><div class="caption"><strong>ビル</strong><span>BUILDING</span></div></div>
    <div class="card"><div class="photo" role="img" aria-label="緑に囲まれた住宅の写真" style="background:linear-gradient(180deg,#9ec2e4,#b9b2a3 55%,#6f8f54)"></div><div class="caption"><strong>投資用物件</strong><span>REAL ESTATE INVESTMENT</span></div></div>
  </div>
</section>

<section class="office">
  <h2 class="section-title" style="top:2770px">OFFICE</h2>
  <p class="section-kana" style="top:2806px;color:var(--muted)">店舗情報</p>
  <div class="office-photo" role="img" aria-label="本店の受付カウンターの写真" style="left:190px;top:2856px;width:260px;height:220px;background:linear-gradient(160deg,#a8895f,#4a3826)"></div>
  <div class="office-info" style="left:620px;top:2880px">
    <h3>仙台本店</h3>
    <p>TEL 000-123-4567（賃貸専用）<br>営業 10:00〜19:00（水曜・祝日定休）<br>宮城県仙台市青葉区一番町 0-0-0 本館ビル1F</p>
    <div class="pill-btn map-btn">MAP</div>
  </div>
  <div class="office-info" style="left:330px;top:3140px">
    <h3>大阪店</h3>
    <p>TEL 000-765-4321（売買専用）<br>営業 10:00〜19:00（水曜定休）<br>大阪府大阪市北区梅田 0-0-0</p>
    <div class="pill-btn map-btn">MAP</div>
  </div>
  <div class="office-photo" role="img" aria-label="会議室の写真" style="left:600px;top:3136px;width:400px;height:220px;background:linear-gradient(180deg,#8e8a86,#3e3a38)"></div>
</section>

<div class="to-top"><svg width="14" height="9" viewBox="0 0 14 9"><path d="M1 8 L7 2 L13 8" fill="none" stroke="#ff8a2b" stroke-width="2"/></svg></div>

<footer class="site-footer">
  <div class="footer-brand">SELECTA</div>
  <nav class="footer-nav">
    <a href="#">トップページ</a><a href="#">会社概要</a><a href="#">プライバシーポリシー</a><a href="#">ご利用上の注意</a><a href="#">お問合せ</a><a href="#">メール</a><a href="#">リンク</a>
  </nav>
  <p class="copyright">Copyright © SELECTA All Rights Reserved.</p>
</footer>

</body>
</html>
```